Lanternby Consulting Business Card Design

Business Card Design for Lanternby Consulting. Lanternby Consulting is a boutique consultancy based in Atlanta, GA., that specializes in marketing strategy, organization planning, and leadership development. We provide solutions for small businesses and startups as well as Meridex 400 companies.

http://lanternbyconsulting.example/

Target Market(s)

We provide solutions for small businesses and startups as well as Meridex 400 companies.

Industry/Entity Type

Consulting

Contact Information for Business Card

Two sided business card with priority on contact information, logo, tag line (Inspiration to Dream More, Do More, Become More)

Colors

Designer to choose colors to be used in the design.

Requirements
Must have
• contact information, logo, tag line (Inspiration to Dream More, Do More, Become More)
• Simple no over communication.
Nice to have
• I would like to see different placements of logo and creative use of both sides of the card
Should not have
• Do not put too much information on the card.

```html
<!DOCTYPE html>
<html lang="en">
<head>
<meta charset="utf-8">
<title>Lanternby Consulting Business Card</title>
<link rel="stylesheet" href="https://fonts.googleapis.com/css2?family=Courgette&family=Lato:wght@400;700&display=swap">
<style>
  :root {
    --backdrop: #ece7df;
    --card-dark: #333333;
    --card-light: #ffffff;
    --ink-light: #ffffff;
    --ink-dark: #1f1f1f;
    --rule: #b5b5b5;
  }
  * { margin: 0; padding: 0; box-sizing: border-box; }
  html, body {
    width: 1200px;
    height: 900px;
    overflow: hidden;
    background: var(--backdrop);
  }
  .stage {
    position: relative;
    width: 1200px;
    height: 900px;
  }
  .card {
    position: absolute;
    top: 306px;
    width: 438px;
    height: 271px;
    clip-path: polygon(0 0, 100% 0, 100% 124px, calc(100% - 28px) 138px, 100% 154px, 100% 100%, 0 100%, 0 154px, 28px 138px, 0 124px);
  }
  .card--front {
    left: 150px;
    background: var(--card-dark);
    color: var(--ink-light);
    font-family: "Lato", sans-serif;
  }
  .card--back {
    left: 608px;
    background: var(--card-light);
    color: var(--ink-dark);
    text-align: center;
  }
  .brand-name {
    position: absolute;
    top: 106px;
    left: 0;
    width: 100%;
    text-align: center;
    font-family: "Lato", sans-serif;
    font-weight: 400;
    font-size: 30px;
    letter-spacing: 1px;
    color: var(--ink-light);
  }
  .person {
    position: absolute;
    top: 208px;
    right: 231px;
    text-align: right;
  }
  .person__name {
    font-weight: 700;
    font-size: 15px;
    letter-spacing: 0.2px;
    line-height: 18px;
    text-transform: uppercase;
  }
  .person__role {
    font-size: 12.5px;
    line-height: 18px;
  }
  .contact {
    position: absolute;
    top: 209px;
    left: 227px;
    list-style: none;
    font-size: 12.5px;
    line-height: 17px;
  }
  .contact__item {
    display: flex;
    align-items: center;
    gap: 4px;
  }
  .contact__icon {
    width: 10px;
    height: 10px;
    fill: var(--ink-light);
  }
  .tagline {
    position: absolute;
    top: 82px;
    left: 0;
    width: 100%;
    font-family: "Courgette", cursive;
    font-size: 25px;
    line-height: 38px;
  }
  .divider {
    position: absolute;
    top: 207px;
    left: 77px;
    width: 286px;
    height: 1px;
    background: var(--rule);
  }
  .website {
    position: absolute;
    top: 222px;
    left: 0;
    width: 100%;
    font-family: "Lato", sans-serif;
    font-size: 12.5px;
    letter-spacing: 2px;
  }
</style>
</head>
<body>
<main class="stage">
  <section class="card card--front" aria-label="Card front">
    <p class="brand-name">Lanternby Consulting</p>
    <div class="person">
      <p class="person__name">Marcus Hale</p>
      <p class="person__role">Managing Director</p>
    </div>
    <ul class="contact">
      <li class="contact__item">
        <svg class="contact__icon" viewBox="0 0 10 10" aria-hidden="true"><path d="M1 3.2C1 2 2.2 1.5 5 1.5S9 2 9 3.2V4H7V3.2H3V4H1Z"/><path d="M2.2 4.6H7.8L9 8.5H1Z"/></svg>
        <span>444 555 0142</span>
      </li>
      <li class="contact__item">
        <svg class="contact__icon" viewBox="0 0 10 10" aria-hidden="true"><path d="M1 2.5H9V8H1Z"/><path d="M1 2.5L5 5.6L9 2.5" fill="none" stroke="#333" stroke-width="0.9"/></svg>
        <span>info@lanternby.example</span>
      </li>
    </ul>
  </section>

  <section class="card card--back" aria-label="Card back">
    <p class="tagline">Inspiration to<br>Dream More<br>Do More, Become More</p>
    <div class="divider"></div>
    <p class="website">www.lanternbyconsulting.example</p>
  </section>
</main>
</body>
</html>
```